Meridian Handsets business card design

I would like to see some designs for a business card for Meridian Handsets. I would like the business card to be double sided. It will need to have a similar colour / look and feel to our website www.meridianhandsets.com.au I have also attached our latest flyer. Final designs to be handed over in Photoshop format so that I can edit the business card when needed please.

Industry/Entity Type

Business

Contact Information for Business Card

Gavin Thornley
sales@meridianhandsets.com.au
Business Development Manager
ph: (08) 6197 5821
www.meridianhandsets.com.au

Font styles to use
Serif
Sans Serif

Requirements
Must have
• If you could please utilise our colour scheme as seen on our website and the attached flyer.
• I would also like the final design to be in a Photoshop format so that I can edit it when needed please.

```html
<!DOCTYPE html>
<html lang="en">
<head>
<meta charset="UTF-8">
<title>Meridian Handsets – Business Card</title>
<link rel="stylesheet" href="https://fonts.googleapis.com/css2?family=Open+Sans:wght@300;400;600&display=swap">
<style>
  :root {
    --canvas-bg: #e8e6e3;
    --card-white: #ffffff;
    --ink-dark: #2b2b2b;
    --ink-body: #1e1e1e;
    --brand-blue: #1a7bbd;
    --back-blue-light: #3a78bf;
    --back-blue-dark: #0f55a6;
    --text-light: #ffffff;
  }
  * { margin: 0; padding: 0; box-sizing: border-box; }
  html, body {
    width: 1200px;
    height: 1000px;
    overflow: hidden;
    background: var(--canvas-bg);
    font-family: "Open Sans", Arial, sans-serif;
  }
  .stage { position: relative; width: 1200px; height: 1000px; }
  .card {
    position: absolute;
    left: 265px;
    width: 665px;
    height: 397px;
    border-radius: 22px;
    box-shadow: 0 6px 16px rgba(0,0,0,0.22);
    overflow: hidden;
  }
  .card-front { top: 73px; background: var(--card-white); }
  .card-back {
    top: 532px;
    background: radial-gradient(ellipse at 50% 40%, var(--back-blue-light) 0%, var(--back-blue-dark) 75%);
    text-align: center;
  }
  .front-wordmark {
    position: absolute;
    left: 32px;
    top: 70px;
    font-size: 38px;
    font-weight: 600;
    color: var(--ink-dark);
    letter-spacing: -0.5px;
  }
  .holder-name {
    position: absolute;
    left: 33px;
    top: 198px;
    font-size: 21px;
    font-weight: 600;
    color: var(--brand-blue);
  }
  .holder-title {
    position: absolute;
    left: 33px;
    top: 228px;
    font-size: 16px;
    color: var(--ink-body);
  }
  .contact-list {
    position: absolute;
    left: 33px;
    top: 286px;
    list-style: none;
  }
  .contact-list li {
    display: flex;
    align-items: center;
    height: 25px;
    font-size: 16px;
    color: var(--ink-body);
  }
  .contact-icon { width: 14px; height: 14px; margin-right: 9px; fill: var(--brand-blue); }
  .back-wordmark {
    margin-top: 168px;
    font-size: 44px;
    font-weight: 600;
    color: var(--text-light);
    letter-spacing: -0.5px;
  }
  .back-tagline {
    margin-top: 2px;
    font-size: 22px;
    font-weight: 300;
    color: var(--text-light);
  }
</style>
</head>
<body>
<main class="stage">
  <section class="card card-front" aria-label="Card front">
    <div class="front-wordmark">Meridian Handsets</div>
    <div class="holder-name">Gavin Thornley</div>
    <div class="holder-title">Business Development Manager</div>
    <ul class="contact-list">
      <li>
        <svg class="contact-icon" viewBox="0 0 16 16" aria-hidden="true"><path d="M1 5c0-2 3-3 7-3s7 1 7 3v1h-4V5H5v1H1zM4 7h8l2 6H2z"/></svg>
        (08) 6197 5821
      </li>
      <li>
        <svg class="contact-icon" viewBox="0 0 16 16" aria-hidden="true"><path d="M1 3h14v10H1z M2 4l6 5 6-5" stroke="#fff" stroke-width="1"/></svg>
        sales@meridianhandsets.com.au
      </li>
      <li>
        <svg class="contact-icon" viewBox="0 0 16 16" aria-hidden="true"><circle cx="8" cy="8" r="7"/><path d="M1 8h14M8 1c3 3 3 11 0 14M8 1c-3 3-3 11 0 14" stroke="#fff" stroke-width="1" fill="none"/></svg>
        www.meridianhandsets.com.au
      </li>
    </ul>
  </section>

  <section class="card card-back" aria-label="Card back">
    <div class="back-wordmark">Meridian Handsets</div>
    <div class="back-tagline">Phone systems for your business</div>
  </section>
</main>
</body>
</html>
```